Web design

We need the design for the logo and website for a women fashion website. No coding required. The colors used should be neutral (maybe with a light touch of color), the style should be modern, slightly luxurious, not too crowded. The target market is young professionals who love trendy clothes.
Updates

Need extra days to review

Target Market(s)

Young professionals

Industry/Entity Type

Apparel

Number of Pages Required

5+ page

Font styles to use
Sans Serif
Other font styles liked:
• Montserrat, Engravers Gothic, Benton Sans, gotham-book

Colors

Designer to choose colors to be used in the design.

```html
<!DOCTYPE html>
<html lang="en">
<head>
<meta charset="utf-8">
<title>LUMA — Women's Fashion</title>
<link href="https://fonts.googleapis.com/css2?family=Baloo+2:wght@700;800&family=Roboto:wght@300;400;500;700&display=swap" rel="stylesheet">
<style>
:root{
  --gold:#f5cf72;
  --gold-deep:#e9b84a;
  --ink:#2a2637;
  --text:#555;
  --muted:#888;
  --line:#ebebeb;
  --hot:#e02b2b;
  --white:#fff;
}
*{box-sizing:border-box;margin:0;padding:0}
html,body{width:1200px;height:3578px;overflow:hidden}
body{position:relative;background:var(--white);font-family:"Roboto",sans-serif;color:var(--ink)}
.abs{position:absolute}
.display{font-family:"Baloo 2",sans-serif;font-weight:800;letter-spacing:-.5px}
a{color:inherit;text-decoration:none}

.topbar{left:0;top:0;width:1200px;height:46px;background:var(--gold);display:flex;align-items:center;justify-content:center;gap:14px;font-size:13px}
.topbar .close{position:absolute;right:80px;top:14px;font-size:14px;color:#c9a54e}

.hero{left:0;top:46px;width:1200px;height:628px;background:linear-gradient(100deg,#f2dfd6 0%,#eed3c6 45%,#d9b7a6 60%,#eed6cb 80%,#f2ded4 100%)}
.wordmark{font-family:"Roboto",sans-serif;font-weight:500;font-size:28px;letter-spacing:1px;color:var(--ink)}
.nav{top:93px;left:301px;display:flex;gap:48px;font-size:13px}
.search{left:597px;top:79px;width:222px;height:40px;background:#fff;border:1px solid #e3e3e3;font-size:12px;color:#bbb;padding:12px 14px}
.search svg{position:absolute;right:12px;top:11px}
.icons{top:84px;left:872px;display:flex;gap:26px;align-items:center}
.badge{position:absolute;top:-6px;right:-8px;width:14px;height:14px;border-radius:50%;background:var(--gold);font-size:9px;display:flex;align-items:center;justify-content:center}
.eyebrow{left:154px;top:266px;font-size:12px;letter-spacing:1.5px}
.btn{background:var(--gold);border-radius:30px;display:flex;align-items:center;justify-content:center;gap:12px;font-weight:500;color:var(--ink)}
.spot{width:30px;height:30px;border-radius:50%;background:var(--gold);border:4px solid rgba(255,255,255,.45);font-size:12px;display:flex;align-items:center;justify-content:center}
.mini{left:899px;top:540px;width:210px;height:93px;background:#fff;display:flex}
.mini .ph{width:90px;height:93px;background:linear-gradient(160deg,#2f4578,#1d2a4d)}
.mini .txt{padding:12px 10px;font-size:12px;line-height:19px}
.mini .go{position:absolute;right:0;bottom:0;width:26px;height:26px;background:var(--gold);display:flex;align-items:center;justify-content:center}
.pager{left:1094px;top:326px;font-size:11px}
.pager i{display:block;width:10px;height:10px;border:1px solid #999;border-radius:50%;margin-bottom:18px}
.pager i.on{background:var(--ink);border-color:var(--ink)}

.features{left:0;top:674px;width:1200px;height:87px;border-bottom:1px solid var(--line);background:#fafafa}
.feat{top:0;height:87px;display:flex;align-items:center;gap:20px}
.feat b{display:block;font-weight:400;font-size:14px;margin-bottom:6px}
.feat span{font-size:11.5px;color:var(--muted)}
.vline{top:0;width:1px;height:87px;background:var(--line)}

.promo{top:807px;height:314px}
.promo-left{left:154px;width:509px;background:linear-gradient(90deg,#f4f1ee 0%,#ece6e1 45%,#b9745f 62%,#8d3b37 72%,#cfc3b8 100%)}
.promo-right{left:689px;width:354px;background:linear-gradient(90deg,#0e5a72 0%,#13657d 55%,#c9c5c0 75%,#14627a 100%)}
.sm-btn{border-radius:20px;font-size:10px;gap:8px}

h2.title{width:1200px;text-align:center;font-weight:500;font-size:24px}

.card{width:205px}
.card .img{height:262px;position:relative}
.card .tag{position:absolute;left:10px;top:10px;font-size:9px;padding:2px 9px;border-radius:10px}
.tag.off{background:var(--ink);color:#fff}
.tag.sold{background:var(--gold);color:var(--ink)}
.tag.hot{background:var(--hot);color:#fff}
.card .tools{position:absolute;right:8px;top:10px;display:flex;gap:6px}
.card .tools i{width:18px;height:18px;border-radius:50%;background:rgba(255,255,255,.85);border:1px solid #ddd}
.card .cart{position:absolute;left:0;bottom:0;width:100%;height:28px;background:var(--gold);font-size:11px;font-weight:500;display:flex;align-items:center;justify-content:center}
.card .name{font-size:13px;color:#777;margin:14px 2px 10px}
.card .price{font-size:14px;margin-left:2px}

.fashion{left:0;top:1608px;width:1200px;height:410px;background:linear-gradient(90deg,#e9e6df 0%,#c7b9a4 20%,#bf7a6e 32%,#a68870 48%,#eeeae3 62%,#f6f4f0 100%)}

.feed-title{top:2960px;width:1200px;text-align:center;font-size:24px;font-weight:500;color:#c8457a}
.tile{top:3024px;width:197px;height:210px}

.footer{left:0;top:3239px;width:1200px;height:339px;background:var(--ink);color:#fff}
.footer h4{font-weight:400;font-size:14px;position:absolute}
.footer .links{font-size:12.5px;line-height:28px;color:#ddd}
.news-in{left:742px;top:159px;width:173px;height:41px;border:1px solid var(--gold);font-size:12px;color:var(--gold);padding:13px 16px}
.news-btn{left:915px;top:159px;width:128px;height:41px;border:1px solid var(--gold);background:var(--ink);color:var(--gold);font-size:11px;letter-spacing:2px;font-weight:700;display:flex;align-items:center;justify-content:center}
.social{display:flex;gap:16px;align-items:center;font-size:10px;color:#ccc}
.social i{width:17px;height:17px;border:1.5px solid #ccc;border-radius:4px}
.copy{top:294px;width:1200px;text-align:center;font-size:10px;color:#888}
</style>
</head>
<body>

<div class="abs topbar">
  <svg width="30" height="18" viewBox="0 0 30 18" fill="none" stroke="#2a2637" stroke-width="1.4"><rect x="8" y="2" width="14" height="10"/><path d="M22 5h4l3 4v3h-7"/><circle cx="12" cy="14" r="2"/><circle cx="25" cy="14" r="2"/><path d="M1 5h5M3 8h4"/></svg>
  <span>Free U.S. shipping on orders over $200</span>
  <span class="close">✕</span>
</div>

<section class="abs hero" role="img" aria-label="Photo of a smiling woman with long wavy hair and sunglasses in a grey knit top and denim, against a warm peach wall"></section>

<div class="abs wordmark" style="left:157px;top:84px">LUMA</div>
<nav class="abs nav"><a>Latest Arivals</a><a>Clothes ⌄</a><a>On Sale</a></nav>
<div class="abs search">Search<svg width="16" height="16" viewBox="0 0 16 16" fill="none" stroke="#aaa" stroke-width="1.5"><circle cx="7" cy="7" r="5"/><path d="M11 11l4 4"/></svg></div>
<div class="abs icons">
  <svg width="22" height="24" viewBox="0 0 22 24" fill="none" stroke="#2a2637" stroke-width="1.6"><circle cx="11" cy="7" r="5"/><path d="M2 23c0-5 4-8 9-8s9 3 9 8"/></svg>
  <span style="position:relative"><svg width="24" height="22" viewBox="0 0 24 22" fill="none" stroke="#2a2637" stroke-width="1.6"><path d="M12 20S2 13 2 7a5 5 0 0 1 10-1 5 5 0 0 1 10 1c0 6-10 13-10 13z"/></svg><span class="badge">1</span></span>
  <span style="position:relative"><svg width="22" height="24" viewBox="0 0 22 24" fill="none" stroke="#2a2637" stroke-width="1.6"><path d="M3 8h16l-1 15H4z"/><path d="M7 8V5a4 4 0 0 1 8 0v3"/></svg><span class="badge">1</span></span>
  <svg width="26" height="26" viewBox="0 0 26 26"><circle cx="13" cy="13" r="12" fill="#1f3a8a"/><path d="M3 13h20M13 3v20" stroke="#fff" stroke-width="5"/><path d="M3 13h20M13 3v20" stroke="#d22" stroke-width="2.6"/></svg>
</div>

<div class="abs eyebrow">New Arrival</div>
<h1 class="abs display" style="left:154px;top:290px;font-size:54px;line-height:58px">Get Latest<br>Trends On Reveal</h1>
<p class="abs" style="left:156px;top:426px;font-size:14px;line-height:24px;color:#444">Does it get any more summertime than a classic summer dress?<br>This wardrobe icon has earned its rightful place on our list of sunshine.</p>
<a class="abs btn" style="left:154px;top:504px;width:152px;height:45px;font-size:14px">Shop Now <svg width="22" height="10" viewBox="0 0 22 10" fill="none" stroke="#2a2637" stroke-width="1.8"><path d="M0 5h20M16 1l4 4-4 4"/></svg></a>

<div class="abs spot" style="left:634px;top:363px">1</div>
<div class="abs mini">
  <div class="ph" role="img" aria-label="Navy checkered short skirt product photo"></div>
  <div class="txt">White short<br>checkered skirt<br><b style="font-weight:500">$119.00</b></div>
  <span class="go"><svg width="8" height="10" viewBox="0 0 8 10" fill="none" stroke="#2a2637" stroke-width="1.5"><path d="M2 1l4 4-4 4"/></svg></span>
</div>
<div class="abs spot" style="left:881px;top:618px">2</div>
<div class="abs pager"><i></i><i class="on"></i><i></i></div>
<div class="abs" style="left:1113px;top:353px;font-size:11px">— &nbsp;02</div>

<div class="abs features"></div>
<div class="abs feat" style="left:184px;top:674px">
  <svg width="44" height="44" viewBox="0 0 44 44" fill="none" stroke="#2a2637" stroke-width="1.5"><circle cx="21" cy="23" r="16"/><path d="M5 23h32M21 7c-6 8-6 24 0 32M21 7c6 8 6 24 0 32"/><circle cx="33" cy="11" r="7" fill="#f5cf72"/></svg>
  <div><b>Shipping Worldwide</b><span>Fast Free Shipping</span></div>
</div>
<div class="abs vline" style="left:445px;top:674px"></div>
<div class="abs feat" style="left:502px;top:674px">
  <svg width="46" height="36" viewBox="0 0 46 36" fill="none" stroke="#2a2637" stroke-width="1.5"><rect x="2" y="4" width="26" height="20"/><path d="M28 10h9l6 7v7H28z"/><circle cx="11" cy="28" r="4"/><circle cx="36" cy="28" r="4"/><rect x="6" y="10" width="12" height="6" fill="#f5cf72" stroke="none"/></svg>
  <div><b>Free Us Delivery</b><span>On orders over $200!</span></div>
</div>
<div class="abs vline" style="left:750px;top:674px"></div>
<div class="abs feat" style="left:802px;top:674px">
  <svg width="48" height="46" viewBox="0 0 48 46" fill="none" stroke="#2a2637" stroke-width="1.5"><path d="M16 12l16-8 14 8v18l-14 8-16-8z"/><path d="M16 12l16 8 14-8M32 20v18"/><circle cx="12" cy="34" r="9" fill="#f5cf72"/><path d="M8 34a4 4 0 1 1 4 4M8 31v3h3"/></svg>
  <div><b>30 Days Return</b><span>within 30 days for an exchange</span></div>
</div>

<div class="abs promo promo-left" role="img" aria-label="Woman in a knit beanie, red scarf and denim browsing a clothing boutique"></div>
<div class="abs" style="left:207px;top:868px;font-size:19px;font-weight:500">The Hotlist of</div>
<div class="abs display" style="left:207px;top:886px;font-size:42px;line-height:52px">SUMMER</div>
<div class="abs" style="left:181px;top:938px"><i style="display:block;width:6px;height:6px;border-radius:50%;background:var(--gold);margin-bottom:11px"></i><i style="display:block;width:6px;height:6px;border-radius:50%;background:#bbb;margin-bottom:11px"></i><i style="display:block;width:6px;height:6px;border-radius:50%;background:#bbb"></i></div>
<div class="abs" style="left:211px;top:950px;font-size:12.5px;line-height:24px;color:#555">The 12 Biggest Spring &amp;<br>Summer 2021 Trends</div>
<a class="abs btn sm-btn" style="left:208px;top:1011px;width:109px;height:28px">Shop Now <svg width="16" height="8" viewBox="0 0 16 8" fill="none" stroke="#2a2637" stroke-width="1.5"><path d="M0 4h14M11 1l3 3-3 3"/></svg></a>

<div class="abs promo promo-right" role="img" aria-label="Woman in a polka-dot shirt and sunglasses in front of a teal door"></div>
<div class="abs display" style="left:721px;top:910px;font-size:32px;line-height:42px;color:#fff">Street Style</div>
<div class="abs" style="left:721px;top:957px;font-size:17px;letter-spacing:2px;color:#fff">Has it Own Rules</div>
<a class="abs btn sm-btn" style="left:721px;top:1001px;width:89px;height:27px">Shop Now <svg width="14" height="8" viewBox="0 0 14 8" fill="none" stroke="#2a2637" stroke-width="1.5"><path d="M0 4h12M9 1l3 3-3 3"/></svg></a>
<div class="abs" style="left:731px;top:1050px;display:flex;gap:9px"><i style="width:6px;height:6px;border-radius:50%;background:#fff"></i><i style="width:6px;height:6px;border-radius:50%;border:1px solid #fff"></i><i style="width:6px;height:6px;border-radius:50%;border:1px solid #fff"></i></div>

<h2 class="abs title" style="left:0;top:1166px">Latest Collection</h2>

<div class="abs card" style="left:154px;top:1245px">
  <div class="img" role="img" aria-label="Model in a yellow floral sundress" style="background:linear-gradient(180deg,#e4ecef,#d9e3e6 60%,#e9d27a 100%)"><span class="tag off">70% off</span><span class="tools"><i></i><i></i></span><span class="cart">ADD TO CART</span></div>
  <div class="name">Textured vegan leather</div><div class="price">$ 69.00</div>
</div>
<div class="abs card" style="left:382px;top:1245px">
  <div class="img" role="img" aria-label="Model in a rust jumpsuit and dark long coat among plants" style="background:linear-gradient(90deg,#6f7d5a,#a2583d 45%,#2b2a2e 70%,#7c8d66)"><span class="tag sold">SOLD</span><span class="tools"><i></i></span></div>
  <div class="name">Textured vegan leather</div><div class="price">$ 69.00</div>
</div>
<div class="abs card" style="left:614px;top:1245px">
  <div class="img" role="img" aria-label="Model in a denim jacket and floral skirt on a city street" style="background:linear-gradient(180deg,#b8bfc6,#34507f 45%,#e6c34e 75%,#9a9a9a)"><span class="tag hot">HOT</span><span class="tools"><i></i><i></i></span></div>
  <div class="name">Textured vegan leather</div><div class="price">$ 69.00</div>
</div>
<div class="abs card" style="left:839px;top:1245px">
  <div class="img" role="img" aria-label="Model in a mustard dress seated in a cafe reading" style="background:linear-gradient(180deg,#8a8d6a,#c98a2e 50%,#e0a23a 75%,#9b7b58)"><span class="tools"><i></i><i></i></span></div>
  <div class="name">Textured vegan leather</div><div class="price">$ 69.00</div>
</div>

<div class="abs fashion" role="img" aria-label="Woman in a pink dress seated on a rattan chair in a bright boutique"></div>
<div class="abs" style="left:688px;top:1706px;font-size:22px;font-weight:500;color:#333">FIND YOUR</div>
<div class="abs display" style="left:686px;top:1734px;font-size:44px;line-height:54px;color:var(--gold-deep)">PERFECT FASHION</div>
<div class="abs" style="left:692px;top:1804px;font-size:14px;line-height:24px;color:#333">Contemporary wardrobe staples and authentic style<br>for the modern man and women.</div>
<a class="abs btn" style="left:685px;top:1874px;width:150px;height:43px;font-size:14px">Shop Now <svg width="22" height="10" viewBox="0 0 22 10" fill="none" stroke="#2a2637" stroke-width="1.8"><path d="M0 5h20M16 1l4 4-4 4"/></svg></a>

<h2 class="abs title" style="left:0;top:2063px">Trending Looks Near You</h2>

<div class="abs card" style="left:28px;top:2132px"><div class="img" role="img" aria-label="Model in a cream and yellow midi dress" style="background:linear-gradient(180deg,#f1efec,#ebe3c9 55%,#e4cf79)"><span class="tag off">70% off</span><span class="tools"><i></i><i></i></span><span class="cart">ADD TO CART</span></div><div class="name">Textured vegan leather</div><div class="price">$ 69.00</div></div>
<div class="abs card" style="left:269px;top:2132px"><div class="img" role="img" aria-label="Model in a sage green button dress" style="background:linear-gradient(180deg,#eeeceb,#8a9a6c 45%,#7e8f60)"><span class="tag sold">SOLD</span><span class="tools"><i></i><i></i></span></div><div class="name">Textured vegan leather</div><div class="price">$ 69.00</div></div>
<div class="abs card" style="left:508px;top:2132px"><div class="img" role="img" aria-label="Model in an off-shoulder polka dot blouse" style="background:linear-gradient(180deg,#eeeceb,#e3d3c4 45%,#c9a891)"><span class="tag hot">HOT</span><span class="tools"><i></i><i></i></span></div><div class="name">Textured vegan leather</div><div class="price">$ 69.00</div></div>
<div class="abs card" style="left:749px;top:2132px"><div class="img" role="img" aria-label="Model in a blush blouse with a brown belt" style="background:linear-gradient(180deg,#eeeceb,#ead7cf 50%,#c5907c)"><span class="tools"><i></i><i></i></span></div><div class="name">Textured vegan leather</div><div class="price">$ 69.00</div></div>
<div class="abs card" style="left:978px;top:2132px"><div class="img" role="img" aria-label="Model in a blue chambray shirt dress" style="background:linear-gradient(180deg,#eeeceb,#8797b7 40%,#7385a8)"><span class="tools"><i></i><i></i></span></div><div class="name">Textured vegan leather</div><div class="price">$ 69.00</div></div>

<div class="abs card" style="left:28px;top:2486px"><div class="img" role="img" aria-label="Model in a blue tie-dye sundress" style="background:linear-gradient(180deg,#f1f1f1,#8fb6e0 50%,#3d73c2)"><span class="tools"><i></i><i></i></span></div><div class="name">Textured vegan leather</div><div class="price">$ 69.00</div></div>
<div class="abs card" style="left:269px;top:2486px"><div class="img" role="img" aria-label="Model in a white tropical print dress" style="background:linear-gradient(180deg,#f1f1f1,#e9ece6 45%,#7ca07a 70%,#e27a5b)"><span class="tools"><i></i><i></i></span></div><div class="name">Textured vegan leather</div><div class="price">$ 69.00</div></div>
<div class="abs card" style="left:508px;top:2486px"><div class="img" role="img" aria-label="Model in a yellow scalloped mini dress" style="background:linear-gradient(180deg,#f1f1f1,#f2ec8a 45%,#ece37a)"><span class="tools"><i></i><i></i></span></div><div class="name">Textured vegan leather</div><div class="price">$ 69.00</div></div>
<div class="abs card" style="left:749px;top:2486px"><div class="img" role="img" aria-label="Model in a black batwing dress" style="background:linear-gradient(180deg,#f1f1f1,#2a2a2a 40%,#1c1c1c)"><span class="tools"><i></i><i></i></span></div><div class="name">Textured vegan leather</div><div class="price">$ 69.00</div></div>
<div class="abs card" style="left:978px;top:2486px"><div class="img" role="img" aria-label="Model in a white asymmetric dress" style="background:linear-gradient(180deg,#f1f1f1,#fafafa 50%,#e9e9e9)"><span class="tools"><i></i><i></i></span></div><div class="name">Textured vegan leather</div><div class="price">$ 69.00</div></div>

<a class="abs btn" style="left:524px;top:2847px;width:198px;height:45px;font-size:14px">View All Collection <svg width="22" height="10" viewBox="0 0 22 10" fill="none" stroke="#2a2637" stroke-width="1.8"><path d="M0 5h20M16 1l4 4-4 4"/></svg></a>

<div class="abs feed-title" style="left:0">Follow Our Picturely</div>
<div class="abs tile" style="left:0;background:linear-gradient(180deg,#cfd6de,#b9a487 60%,#d9c3ad)" role="img" aria-label="Woman in a floral dress walking on a beach"></div>
<div class="abs tile" style="left:201px;background:linear-gradient(180deg,#b5502f,#e7c02c 55%,#6a6a70)" role="img" aria-label="Woman in a yellow dress jumping by a wall"></div>
<div class="abs tile" style="left:402px;background:linear-gradient(180deg,#e9e4e0,#d8cfc9 50%,#2b2b2b)" role="img" aria-label="Woman in a black pleated skirt under draped fabric"></div>
<div class="abs tile" style="left:603px;background:linear-gradient(180deg,#7a8a4a,#c8883e 50%,#a33f2d)" role="img" aria-label="Woman in a plaid top in golden light"></div>
<div class="abs tile" style="left:804px;background:linear-gradient(180deg,#e7e8ea,#b88f86 55%,#8f9ba6)" role="img" aria-label="Woman in a tiered tulle dress by the water"></div>
<div class="abs tile" style="left:1005px;width:195px;background:linear-gradient(180deg,#dfe2e5,#c9c3bc 45%,#e9b6ae)" role="img" aria-label="Woman in a black top and pink skirt on a street"></div>

<footer class="abs footer">
  <div class="abs wordmark" style="left:161px;top:78px;color:#fff">LUMA</div>
  <h4 style="left:325px;top:62px">About us</h4>
  <div class="abs links" style="left:325px;top:96px">Store Locator<br>Velora Group<br>Sustainability<br>Fondazione Velora<br>Work with us</div>
  <h4 style="left:499px;top:62px">Legal</h4>
  <div class="abs links" style="left:499px;top:96px">Terms and Conditions of Use<br>Privacy Policy<br>Cookie Policy</div>
  <h4 style="left:742px;top:62px">Sign up for newsletter</h4>
  <div class="abs" style="left:742px;top:97px;font-size:10.5px;line-height:24px;color:#ccc">Subscribe to the newsletter to receive updates about collec-<br>tions, events, campaigns and special projects</div>
  <div class="abs news-in">Your email address</div>
  <div class="abs news-btn">SUBSCRIBE</div>
  <div class="abs social" style="left:742px;top:215px">Follow us <i></i><i></i><i></i></div>
  <div class="abs copy" style="left:0">© LUMA 2020 - 2021 . All Rights Reserved</div>
</footer>

</body>
</html>
```